the look of import selling star-up company

I have attached rhino logo that i like (can be edit) and i wanna turn that in to luxury look. Example like black base and gold logo +luxury looking font.

Company name: Brevan trading Oy
Slogan: Made for the extraordinary.
CEO Juho Kettumaa
Starting to import ceramic nano coatings to cars, in home use and industrial purposes.

Target Market(s)

30-60 year old men and women ho have big money and know what car they drive

Industry/Entity Type

It Company

```html
<!DOCTYPE html>
<html lang="en">
<head>
<meta charset="utf-8">
<title>Brevan trading Oy – Stationery</title>
<link href="https://fonts.googleapis.com/css2?family=Montserrat:wght@500;600&family=Quicksand:wght@400;500&family=Arimo:wght@400;700&display=swap" rel="stylesheet">
<style>
  :root {
    --backdrop: #d4d4d4;
    --paper: #ffffff;
    --ink: #111111;
    --ink-soft: #333333;
    --band: #1d1b1b;
    --faint: #e6e6e6;
    --shadow: 0 4px 6px rgba(0,0,0,0.35);
  }
  * { margin: 0; padding: 0; box-sizing: border-box; }
  html, body { width: 1200px; height: 1200px; overflow: hidden; }
  body { background: var(--backdrop); position: relative; font-family: "Arimo", sans-serif; color: var(--ink); }

  .sheet { position: absolute; background: var(--paper); box-shadow: var(--shadow); overflow: hidden; }

  .mark { position: absolute; border-radius: 50%; border: solid var(--ink); display: flex; align-items: center; justify-content: center; text-align: center;
          font-family: "Montserrat", sans-serif; font-weight: 600; color: var(--ink); line-height: 1.15; }
  .mark--light { border-color: var(--paper); color: var(--paper); }

  /* letterhead */
  .letterhead { left: 25px; top: 47px; width: 603px; height: 845px; }
  .letterhead .mark { left: 248px; top: 34px; width: 106px; height: 106px; border-width: 8px; font-size: 11px; }
  .letterhead__name { position: absolute; left: 0; width: 100%; top: 150px; text-align: center; }
  .letterhead__name span { font-family: "Montserrat", sans-serif; font-weight: 600; font-size: 21px; letter-spacing: 1.6px; border-bottom: 2px solid var(--ink); padding-bottom: 1px; }
  .letter { position: absolute; left: 23px; top: 218px; width: 557px; font-size: 12px; line-height: 14.2px; letter-spacing: 0.6px; text-align: justify; color: var(--ink-soft); }
  .letter__greeting { font-weight: 700; font-size: 12px; margin-bottom: 11px; color: var(--ink); }
  .letter p { margin-bottom: 14.2px; }
  .signoff { position: absolute; left: 23px; top: 684px; width: 150px; border-bottom: 2px solid var(--ink); padding-bottom: 3px; }
  .signoff__name { font-weight: 700; font-size: 13.5px; }
  .signoff__role { font-size: 13.5px; margin-top: 5px; }
  .letterhead__deco { position: absolute; left: 490px; top: 690px; width: 190px; height: 190px; border-radius: 50%; border: 10px solid var(--faint); }
  .letterhead__rule { position: absolute; left: 8px; right: 8px; top: 799px; border-top: 1.5px solid var(--ink); }
  .letterhead__band { position: absolute; left: 8px; right: 8px; top: 805px; height: 28px; background: var(--band); color: var(--paper);
                      font-family: "Quicksand", sans-serif; font-weight: 500; font-size: 19px; letter-spacing: 1.6px; text-align: center; line-height: 28px; }

  /* envelopes */
  .envelope-back { left: 461px; top: 160px; width: 718px; height: 294px; }
  .envelope-back__flap { position: absolute; left: 0; top: 0; width: 718px; height: 80px; }
  .envelope-back .mark { left: 329px; top: 10px; width: 58px; height: 58px; border-width: 4px; font-size: 6px; }

  .envelope-front { left: 461px; top: 503px; width: 718px; height: 295px; }
  .envelope-front .mark { left: 17px; top: 199px; width: 80px; height: 80px; border-width: 6px; font-size: 8.5px; }
  .envelope-front__sender { position: absolute; right: 19px; top: 221px; text-align: right; }
  .envelope-front__name { font-family: "Montserrat", sans-serif; font-weight: 600; font-size: 13.6px; letter-spacing: 1px; padding-bottom: 1px; border-bottom: 1.5px solid var(--ink-soft); padding-left: 40px; }
  .envelope-front__slogan { font-family: "Quicksand", sans-serif; font-size: 13.6px; letter-spacing: 1px; color: var(--ink-soft); margin-top: 1px; }

  /* business cards */
  .card { position: absolute; top: 918px; height: 256px; border-radius: 10px; box-shadow: var(--shadow); overflow: hidden; }
  .card--front { left: 112px; width: 430px; background: var(--paper); }
  .card--back { left: 690px; width: 428px; background: var(--band); }
  .card__name { position: absolute; left: 30px; top: 48px; font-family: "Montserrat", sans-serif; font-weight: 600; font-size: 16px; letter-spacing: 1.2px; }
  .card__contacts { position: absolute; left: 30px; top: 89px; font-family: "Quicksand", sans-serif; font-size: 10.5px; line-height: 13.5px; }
  .card__contacts dl { display: grid; grid-template-columns: auto 1fr; column-gap: 3px; margin-bottom: 11px; }
  .card__contacts dt { font-weight: 700; font-family: "Arimo", sans-serif; font-size: 10px; }
  .card--front .mark { left: 261px; top: 57px; width: 138px; height: 138px; border-width: 10px; font-size: 13px; }
  .card--back .mark { left: 144px; top: 56px; width: 138px; height: 138px; border-width: 10px; font-size: 13px; }
  .card__slogan { position: absolute; left: 0; width: 100%; top: 226px; text-align: center; }
  .card__slogan span { font-family: "Quicksand", sans-serif; font-size: 16px; letter-spacing: 1.4px; color: var(--paper); border-bottom: 1px solid var(--paper); padding-bottom: 1px; }
</style>
</head>
<body>

<section class="sheet letterhead">
  <div class="mark">Brevan<br>trading Oy</div>
  <div class="letterhead__name"><span>BREVAN TRADING OY</span></div>
  <div class="letter">
    <div class="letter__greeting">Dear Mr. Juho Kettumaa</div>
    <p>Lorem Ipsum is simply dummy text of the printing and typesetting industry. Lorem Ipsum has been the industry's standard dummy text ever since the 1500s, when an unknown printer took a galley of type and scrambled it to make a type specimen book. It has survived not only five centuries, but also the leap into electronic typesetting, remaining essentially unchanged. It was popularised in the 1960s with the release of Lettrex sheets containing Lorem Ipsum passages, and more recently with desktop publishing software like Pagewright Studio including versions of Lorem Ipsum.</p>
    <p>Contrary to popular belief, Lorem Ipsum is not simply random text. It has roots in a piece of classical Latin literature from 45 BC, making it over 2000 years old. A Latin professor at Harrowgate College in Virginia, looked up one of the more obscure Latin words, consectetur, from a Lorem Ipsum passage, and going through the cites of the word in classical literature, discovered the undoubtable source. Lorem Ipsum comes from sections 1.10.32 and 1.10.33 of "de Finibus Bonorum et Malorum" (The Extremes of Good and Evil) by Tullius Marcellus, written in 45 BC. This book is a treatise on the theory of ethics, very popular during the Renaissance. The first line of Lorem Ipsum, "Lorem ipsum dolor sit amet..", comes from a line in section 1.10.32.</p>
    <p>The standard chunk of Lorem Ipsum used since the 1500s is reproduced below for those interested. Sections 1.10.32 and 1.10.33 from "de Finibus Bonorum et Malorum" by Tullius Marcellus are also reproduced in their exact original form, accompanied by English versions from the 1914 translation by H. Rackwell.</p>
    <p>It is a long established fact that a reader will be distracted by the readable content of a page when looking at its layout. The point of using Lorem Ipsum is that it has a more-or-less normal distribution of letters, as opposed to using 'Content here, content here', making it look like readable English. Many desktop publishing packages and web page editors now use Lorem Ipsum as their default model text, and a search for 'lorem ipsum'</p>
  </div>
  <div class="signoff">
    <div class="signoff__name">Mika Aalto</div>
    <div class="signoff__role">Graphic Designer</div>
  </div>
  <div class="letterhead__deco" aria-hidden="true"></div>
  <div class="letterhead__rule"></div>
  <div class="letterhead__band">MADE FOR THE EXTRAORDINARY</div>
</section>

<section class="sheet envelope-back">
  <svg class="envelope-back__flap" viewBox="0 0 718 80" aria-hidden="true">
    <path d="M0 0 H718 L682 68 Q676 80 662 80 H58 Q44 80 38 68 Z" fill="#1d1b1b"/>
  </svg>
  <div class="mark mark--light">Brevan<br>trading Oy</div>
</section>

<section class="sheet envelope-front">
  <div class="mark">Brevan<br>trading Oy</div>
  <div class="envelope-front__sender">
    <div class="envelope-front__name">BREVAN TRADING OY</div>
    <div class="envelope-front__slogan">Made for the extraordinary</div>
  </div>
</section>

<section class="card card--front">
  <div class="card__name">BREVAN TRADING OY</div>
  <div class="card__contacts">
    <dl><dt>Call</dt><dd>- 012-3456-789</dd><dt>Fax</dt><dd>- 012-3456-780</dd></dl>
    <dl><dt>Web -</dt><dd>www.brevantradingoy.com</dd><dt>Mail</dt><dd>- brevantradingoy.com</dd></dl>
    <dl><dt>Add</dt><dd>- Your floor, Your Street,<br>&nbsp;&nbsp;New Yourk-9213</dd></dl>
  </div>
  <div class="mark">Brevan<br>trading Oy</div>
</section>

<section class="card card--back">
  <div class="mark mark--light">Brevan<br>trading Oy</div>
  <div class="card__slogan"><span>Made for the extraordinary</span></div>
</section>

</body>
</html>
```